New Label Design Project - Quillfen Dermal

Label Design Brief - Quillfen Dermal
Label Panel Dimensions 1.25" W x 2.375" H (front/back panel)
Hello - our company develops novel products for the skin, & hair care industry as well as dietary supplements. We're looking for a label design for a new product. The product is a premium Topical hair loss/growth serum. I attached the brand logo & 2 other sister products along with some competitive products.
The product is a topical natural hair loss serum for men & women to regrow new hair and help restore hair loss & thinning hair due to vitamin deficiencies, hormone imbalance & aging. It is a science based efficacious serum with a century’s old medicinal herbal formula.
Attached is our logo & some files of other competition. The label must have an upscale, technology flair to it. The product is clinically effective, leveraged by Ancient Wisdom and Modern Science.
Below are attached files of 2 of our products & other generic competition for your perusal.

https://www.shopvarlo.example/item/K7R2TQ4MPL?ref=lst_featured

https://www.shopvarlo.example/item/K7R3ZN8WDH/ref=lst-redir?pg=1&ref=lst_lowprice

Target Market(s)

men & women age 18-80

Requirements
Must have
• see brief
Should not have
• Please do not have a picture of a man or a women on the label.

```html
<!DOCTYPE html>
<html lang="en">
<head>
<meta charset="utf-8">
<title>Quillfen Dermal – DHT Blocker Growth Activator Label</title>
<link rel="stylesheet" href="https://fonts.googleapis.com/css2?family=Roboto+Condensed:wght@700&family=Dancing+Script:wght@500&display=swap">
<style>
  :root {
    --brown: #6a3217;
    --brown-dark: #57270f;
    --orange: #ee7d22;
    --peach: #f2c7aa;
    --peach-soft: #f8ddca;
    --label-white: #ffffff;
    --page: #efefef;
    --text-white: #ffffff;
  }
  * { box-sizing: border-box; margin: 0; padding: 0; }
  html, body {
    width: 1200px; height: 1200px; overflow: hidden;
    background: var(--page);
  }
  .canvas { position: relative; width: 1200px; height: 1200px; }

  .label {
    position: absolute; left: 240px; top: 128px;
    width: 720px; height: 944px;
    background: var(--label-white);
    border-radius: 18px;
    overflow: hidden;
    font-family: "Roboto Condensed", "Arial Narrow", sans-serif;
    font-weight: 700;
    color: var(--brown);
  }

  .top-band { position: absolute; left: 0; top: 0; width: 720px; height: 60px; }

  .brand {
    position: absolute; left: 0; top: 170px; width: 720px;
    display: flex; align-items: center; justify-content: center; gap: 18px;
  }
  .brand-dot { width: 34px; height: 34px; border-radius: 50%; background: var(--brown); }
  .brand-name { font-size: 52px; letter-spacing: 1px; color: var(--brown); text-transform: uppercase; }

  .claim-box {
    position: absolute; background: var(--brown); color: var(--text-white);
    text-transform: uppercase; line-height: 1;
  }
  .claim-dht {
    left: 90px; top: 307px; width: 193px; height: 189px;
    display: flex; flex-direction: column; align-items: center; justify-content: center;
  }
  .claim-dht .big { font-size: 96px; letter-spacing: 1px; }
  .claim-dht .small { font-size: 36px; letter-spacing: 1px; margin-top: 6px; }

  .claim-growth {
    left: 295px; top: 307px; width: 302px; height: 189px;
    display: flex; flex-direction: column; justify-content: center; padding-left: 14px;
  }
  .claim-growth .line-1 { font-size: 58px; letter-spacing: 1px; }
  .claim-growth .line-2 { font-size: 46px; letter-spacing: 1px; margin-top: 4px; }
  .claim-growth .audience { font-size: 26px; color: var(--orange); margin-top: 10px; }

  .tagline {
    position: absolute; left: 0; top: 540px; width: 720px; text-align: center;
    font-family: "Dancing Script", cursive; font-weight: 500;
    font-size: 28px; color: var(--brown-dark);
  }

  .benefits {
    position: absolute; left: 160px; top: 630px; list-style: none;
    font-size: 30px; line-height: 37px; color: var(--brown-dark);
  }

  .leaf-art {
    position: absolute; left: 366px; top: 590px; width: 236px; height: 260px;
    border-radius: 60% 40% 55% 45%;
    background: radial-gradient(circle at 50% 55%, var(--peach) 0%, var(--peach-soft) 60%, rgba(248,221,202,0) 75%);
  }

  .bottom-band { position: absolute; left: 0; bottom: 0; width: 720px; height: 60px; background: var(--brown); }

  .mortar-art {
    position: absolute; left: 100px; top: 838px; width: 120px; height: 82px;
    border-radius: 50% 50% 46% 46%;
    background: linear-gradient(180deg, var(--orange) 0%, var(--brown) 100%);
  }

  .volume {
    position: absolute; left: 229px; top: 878px; width: 130px; height: 34px;
    border-radius: 17px; background: var(--orange); color: var(--text-white);
    font-size: 24px; display: flex; align-items: center; justify-content: center;
  }
</style>
</head>
<body>
<div class="canvas">
  <div class="label">
    <svg class="top-band" viewBox="0 0 720 60" aria-hidden="true">
      <path d="M0 0 H720 V34 H504 Q490 34 488 48 Q486 58 474 58 H246 Q234 58 232 48 Q230 34 216 34 H0 Z" fill="var(--brown)"/>
    </svg>

    <div class="brand">
      <span class="brand-dot"></span>
      <span class="brand-name">Quillfen Dermal</span>
    </div>

    <div class="claim-box claim-dht">
      <span class="big">DHT</span>
      <span class="small">Blocker</span>
    </div>
    <div class="claim-box claim-growth">
      <span class="line-1">Growth</span>
      <span class="line-2">Activator</span>
      <span class="audience">For Men &amp; Women</span>
    </div>

    <p class="tagline">A premium Topical hair loss/growth serum</p>

    <ul class="benefits">
      <li>Lorem Ipsum</li>
      <li>Lorem Ipsum</li>
      <li>Lorem Ipsum</li>
      <li>Lorem Ipsum</li>
    </ul>

    <div class="leaf-art" role="img" aria-label="Soft peach botanical leaf illustration"></div>

    <div class="bottom-band"></div>
    <div class="mortar-art" role="img" aria-label="Mortar and pestle with herbs illustration"></div>
    <div class="volume">2 FL OZ</div>
  </div>
</div>
</body>
</html>
```